Velvet Stomp Ball Poster

We need a poster design for a local event we are holding in our town. The band playing is called "Tinsel" and the theme is "Glam Rock". We would like to see a design that ties in with the Glam Rock theme and it should be very eyecatching. I have attached a file showing the type of look that you might think is suitable but I am open to suggestions! Thanks so much - I am looking forward to seeing your ideas!!

It also needs to say on the poster that the event is sponsored by the Wandoola CRC (see attached logo) and the Wandoola Progress Association (see attached logo)

Industry/Entity Type

Town

Requirements
Must have
• Must have the following wording...

Calling all Rockers...
The Wandoola Progress Association proudly presents live music by
"Tinsel"
Friday 26th October
7:30pm
Wandoola Hall
Tickets $20 - Available from the Wandoola CRC
Dress - GLAM ROCK

```html
<!DOCTYPE html>
<html lang="en">
<head>
<meta charset="utf-8">
<title>Velvet Stomp Ball – Calling All Rockers</title>
<link rel="stylesheet" href="https://fonts.googleapis.com/css2?family=Inter:wght@100;300;400;700&display=swap">
<style>
  :root {
    --magenta-deep: #8e1f6a;
    --magenta: #c23b92;
    --magenta-bright: #e45fb4;
    --magenta-pale: #f0a6d6;
    --ink: #5a1142;
    --ink-soft: #9c4a80;
    --paper: #ffffff;
  }
  * { margin: 0; padding: 0; box-sizing: border-box; }
  html, body { width: 848px; height: 1200px; overflow: hidden; background: var(--paper); }
  body { font-family: "Inter", Arial, sans-serif; }

  .poster { position: relative; width: 848px; height: 1200px; overflow: hidden; }

  .stage-photo {
    position: absolute; inset: 0;
    background:
      radial-gradient(ellipse at 25% 35%, var(--magenta-pale) 0%, transparent 45%),
      radial-gradient(ellipse at 75% 70%, var(--magenta-bright) 0%, transparent 50%),
      linear-gradient(180deg, var(--magenta) 0%, var(--magenta-bright) 45%, var(--magenta) 75%, var(--magenta-deep) 100%);
  }

  .dash { position: absolute; background: var(--paper); height: 4px; }
  .dash--a { left: 80px;  top: 148px; width: 59px; }
  .dash--b { left: 539px; top: 211px; width: 59px; height: 3px; }
  .dash--c { left: 603px; top: 266px; width: 14px; height: 2px; }
  .dash--d { left: 600px; top: 313px; width: 12px; height: 2px; }
  .dash--e { left: 600px; top: 318px; width: 12px; height: 2px; }

  .band { position: absolute; left: 0; background: var(--paper); }
  .band--calling { top: 480px; width: 848px; height: 120px; }
  .band--all     { top: 600px; width: 405px; height: 118px; }
  .band--rockers { top: 718px; width: 764px; height: 122px; }

  .headline {
    position: absolute; color: var(--ink);
    font-weight: 100; font-size: 143px; line-height: 1;
    letter-spacing: -3px; white-space: nowrap;
  }
  .headline--calling { left: 76px;  top: 477px; }
  .headline--all     { left: 166px; top: 592px; }
  .headline--rockers { left: 76px;  top: 714px; }

  .presenter {
    position: absolute; left: 243px; top: 840px; width: 605px; height: 117px;
    background: var(--paper); padding: 12px 0 0 44px;
  }
  .presenter__host { font-size: 24px; font-weight: 300; color: var(--ink); line-height: 1.15; }
  .presenter__intro { font-size: 22px; font-weight: 300; color: var(--ink-soft); line-height: 1.15; padding-left: 2px; }
  .presenter__band { font-size: 37px; font-weight: 300; color: var(--ink); line-height: 1.2; padding-left: 80px; }

  .details {
    position: absolute; left: 0; top: 957px; width: 517px; height: 120px;
    background: var(--paper); padding: 18px 0 0 40px;
  }
  .details__line { font-size: 20px; font-weight: 300; color: var(--ink-soft); line-height: 1.3; }
  .details__dress { font-size: 34px; font-weight: 300; color: var(--ink); margin-top: 6px; }
  .details__dress strong { font-weight: 700; }

  .sponsors__label {
    position: absolute; left: 49px; top: 1100px;
    font-size: 13px; font-weight: 300; color: var(--paper);
  }
  .sponsor {
    position: absolute; display: flex; align-items: center; gap: 8px;
    font-size: 17px; font-weight: 700; color: var(--paper);
  }
  .sponsor__mark { width: 14px; height: 14px; border-radius: 50%; background: var(--paper); }
  .sponsor--crc { left: 168px; top: 1126px; }
  .sponsor--town { left: 325px; top: 1126px; }
  .sponsor--town .sponsor__mark { border-radius: 0; }

  .info {
    position: absolute; right: 40px; top: 1101px; width: 240px;
    text-align: right; font-size: 12.5px; font-weight: 300; color: var(--paper); line-height: 1.3;
  }
  .info strong { font-weight: 400; }
</style>
</head>
<body>
  <main class="poster">
    <div class="stage-photo" role="img" aria-label="Magenta-tinted concert photo of a drum kit and microphone stand on stage"></div>

    <span class="dash dash--a"></span>
    <span class="dash dash--b"></span>
    <span class="dash dash--c"></span>
    <span class="dash dash--d"></span>
    <span class="dash dash--e"></span>

    <div class="band band--calling"></div>
    <div class="band band--all"></div>
    <div class="band band--rockers"></div>

    <h1>
      <span class="headline headline--calling">CALLING</span>
      <span class="headline headline--all">ALL</span>
      <span class="headline headline--rockers">ROCKERS</span>
    </h1>

    <section class="presenter">
      <p class="presenter__host">The Wandoola Progress Association</p>
      <p class="presenter__intro">proudly presents live music by:</p>
      <p class="presenter__band">“TINSEL”</p>
    </section>

    <section class="details">
      <p class="details__line">Friday 26th October \ 7:30 pm \ Wandoola Hall \</p>
      <p class="details__line">Tickets: $20 \ Available from the Wandoola CRC \</p>
      <p class="details__dress">Dress: <strong>Glam Rock</strong> \</p>
    </section>

    <footer>
      <p class="sponsors__label">Sponsored by:</p>
      <div class="sponsor sponsor--crc"><span class="sponsor__mark"></span>Wandoola CRC</div>
      <div class="sponsor sponsor--town"><span class="sponsor__mark"></span>Wandoola</div>
      <p class="info">For more information visit<br>The Wandoola Community Resource Centre at:<br><strong>www.wandoola-crc.example.au</strong></p>
    </footer>
  </main>
</body>
</html>
```